Business Card Design and New Company Logo

I need a business card design and new company logo for a plant nursery. I will be propagating landscape plants from cuttings and growing them locally for resale, locally grown and nurtured plants for zone 5 climate. I would like a design that depicts the growth of shoots to roots .... locally grown and nurtured landscape plants. Healthy, hardy ornamental trees and shrubs for $4.97. Affordable gardening for all.
Updates
Hello Designers,
Thank you for your submissions. I am going to be out of my office until Monday. I will continue to review submitted designs when I can and posting requests for revisions when time permits on my business trip. I should have a decision next week.
Sincerely,
Marla
Sorry for my delay in choosing a design. I had some unforeseen business and personal events culminate at the same time. I will have my decision by the end of this week and update all by Friday March 21. Thank you for your design submissions and your patience.
Marla
Target Market(s)
Home owners
Industry/Entity Type
Landscape
Contact Information for Business Card
Fernbrook Hollow Nursery
Marla Dunwick
812 Calder Pond Lane
Amherst, MA 01002
413-862-3094
Fernbrook4Hollow@mailvine.net
Look and feel
Each slider illustrates characteristics of the customer's brand and the style your logo design should communicate.

```html
<!DOCTYPE html>
<html lang="en">
<head>
<meta charset="utf-8">
<title>Fernbrook Hollow Nursery – Business Card</title>
<link rel="stylesheet" href="https://fonts.googleapis.com/css2?family=Noto+Sans:wght@300;700&display=swap">
<style>
  :root {
    --card-bg: #4a4a4a;
    --rule: #787878;
    --ink-strong: #2a2a2a;
    --ink: #2c2c2c;
    --tree-dark: #2e2e2e;
    --tree-mid: #3c3c3c;
  }
  html, body {
    margin: 0;
    padding: 0;
    width: 1200px;
    height: 702px;
    overflow: hidden;
    background: var(--card-bg);
  }
  .card {
    position: relative;
    width: 1200px;
    height: 702px;
    background: var(--card-bg);
    font-family: "Noto Sans", sans-serif;
    color: var(--ink);
    overflow: hidden;
  }
  .card > * { position: absolute; margin: 0; line-height: 1; white-space: nowrap; }
  .rule { background: var(--rule); }
  .rule--top { left: 24px; top: 38px; width: 663px; height: 14px; }
  .rule--bottom { left: 22px; top: 652px; width: 1158px; height: 15px; }
  .tree-art {
    left: 697px;
    top: 0;
    width: 503px;
    height: 620px;
    background: radial-gradient(ellipse 60% 50% at 50% 35%, var(--tree-dark) 0%, var(--tree-mid) 70%, var(--card-bg) 100%);
    border-radius: 45% 45% 30% 30%;
  }
  .company-name {
    left: 42px;
    top: 55px;
    font-size: 53px;
    line-height: 66px;
    font-weight: 700;
    color: var(--ink-strong);
  }
  .person-name {
    left: 42px;
    top: 219px;
    font-size: 44px;
    font-weight: 300;
  }
  .street {
    left: 42px;
    top: 274px;
    font-size: 44px;
    font-weight: 300;
  }
  .state-zip {
    right: 548px;
    top: 324px;
    font-size: 24px;
    font-weight: 700;
  }
  .contact-label {
    left: 42px;
    top: 493px;
    font-size: 24px;
    font-weight: 700;
  }
  .phone {
    left: 42px;
    top: 526px;
    font-size: 46px;
    font-weight: 300;
  }
  .email {
    left: 42px;
    top: 590px;
    font-size: 24px;
    font-weight: 700;
  }
</style>
</head>
<body>
  <main class="card">
    <div class="rule rule--top"></div>
    <div class="tree-art" role="img" aria-label="Illustration of a tree with swirling branches and spreading roots"></div>
    <h1 class="company-name">Fernbrook Hollow<br>Nursery</h1>
    <p class="person-name">Marla Dunwick</p>
    <p class="street">812 Calder Pond Lane Amherst</p>
    <p class="state-zip">MA 01002</p>
    <p class="contact-label">Contact:</p>
    <p class="phone">413-862-3094</p>
    <p class="email">Fernbrook4Hollow@mailvine.net</p>
    <div class="rule rule--bottom"></div>
  </main>
</body>
</html>
```